Brightway Freight Biz Card and Stationary
Brightway Freight
Brightway Freight Biz Card and Stationary -
Creative Brief
Modern
Daniel Prescott
President & CEO
P.O. Box 7382 Carverton, SD 58217
d.prescott@tarvo.com
keep it simple

```html
<!DOCTYPE html>
<html lang="en">
<head>
<meta charset="utf-8">
<title>Brightway Freight – Business Card</title>
<link rel="stylesheet" href="https://fonts.googleapis.com/css2?family=Arimo:wght@400;700&display=swap">
<style>
  :root {
    --backdrop: #262729;
    --card: #f7f8f9;
    --brand-blue: #1d5fae;
    --band-blue: #2158a8;
    --band-grey: #b9bcc0;
    --ink: #2e3033;
    --ink-soft: #5d6166;
    --rule: #c6c9cd;
  }
  * { box-sizing: border-box; margin: 0; padding: 0; }
  html, body {
    width: 1200px; height: 954px; overflow: hidden;
    background: var(--backdrop);
    font-family: "Arimo", Arial, sans-serif;
  }
  .stage { position: relative; width: 1200px; height: 954px; }
  .card {
    position: absolute;
    background: linear-gradient(160deg, #ffffff 0%, var(--card) 55%, #e6e9ec 100%);
    border-radius: 26px;
    box-shadow: 0 10px 30px rgba(0,0,0,.45);
    overflow: hidden;
  }
  .card--front { left: 78px; top: 150px; width: 698px; height: 398px; }
  .card--back { left: 434px; top: 509px; width: 673px; height: 412px; }

  .brand { position: absolute; display: flex; align-items: center; gap: 16px; }
  .brand__dot { border-radius: 50%; background: var(--brand-blue); flex: none; }
  .brand__name {
    color: var(--brand-blue); font-weight: 700; text-transform: uppercase;
    letter-spacing: 1px; white-space: nowrap;
  }
  .card--front .brand { left: 40px; top: 52px; }
  .card--front .brand__dot { width: 58px; height: 58px; }
  .card--front .brand__name { font-size: 34px; }

  .holder { position: absolute; right: 58px; top: 122px; text-align: right; }
  .holder__name { font-size: 20px; color: var(--ink); letter-spacing: .5px; }
  .holder__title { font-size: 11px; font-weight: 700; color: var(--ink-soft); margin-top: 5px; letter-spacing: .4px; }

  .band { position: absolute; left: 0; top: 190px; width: 100%; height: 32px; }

  .contacts {
    position: absolute; left: 26px; top: 238px; right: 20px;
    display: flex; font-size: 12px; color: var(--ink-soft); line-height: 1.9;
    text-transform: uppercase; letter-spacing: .3px; white-space: nowrap;
  }
  .contacts__col { padding: 0 18px; border-left: 1px solid var(--rule); }
  .contacts__col:first-child { padding-left: 0; border-left: none; width: 172px; }
  .contacts__col:nth-child(2) { width: 196px; }
  .contacts__col:nth-child(3) { flex: 1; }
  .contacts__label { color: var(--brand-blue); display: inline-block; width: 50px; }

  .card--back .mark {
    position: absolute; left: 62px; top: 70px; width: 210px; height: 210px; border-radius: 50%;
    background: radial-gradient(circle at 40% 35%, #4f9be6 0%, var(--brand-blue) 70%);
  }
  .card--back .brand { right: 30px; bottom: 88px; }
  .card--back .brand__name { font-size: 32px; color: var(--ink); }
</style>
</head>
<body>
<main class="stage">
  <section class="card card--front" aria-label="Business card front">
    <div class="brand">
      <span class="brand__dot"></span>
      <span class="brand__name">Brightway Freight</span>
    </div>
    <div class="holder">
      <p class="holder__name">DANIEL PRESCOTT</p>
      <p class="holder__title">PRESIDENT &amp; CEO</p>
    </div>
    <svg class="band" viewBox="0 0 698 32" preserveAspectRatio="none" aria-hidden="true">
      <polygon points="0,0 178,0 196,20 0,20" fill="var(--band-grey)"/>
      <polygon points="178,12 698,12 698,26 190,26" fill="var(--band-blue)"/>
    </svg>
    <div class="contacts">
      <div class="contacts__col">
        <p>P.O. Box 7382</p>
        <p>Carverton, SD 58217</p>
      </div>
      <div class="contacts__col">
        <p><span class="contacts__label">Phone</span>: 7015550148</p>
        <p><span class="contacts__label">Cell</span>: 7015550192</p>
      </div>
      <div class="contacts__col">
        <p><span class="contacts__label">Fax</span>: 8665550176</p>
        <p><span class="contacts__label">Email</span>: d.prescott@tarvo.com</p>
      </div>
    </div>
  </section>

  <section class="card card--back" aria-label="Business card back">
    <span class="mark"></span>
    <div class="brand">
      <span class="brand__name">Brightway Freight</span>
    </div>
  </section>
</main>
</body>
</html>
```